website design for Company MVR

Our company name MVR(the grand mural limited), need design a website. It is a website that focuses on promoting art design in the world.
We will provide the existing logo design, the new website and logo should be matched to each other. The website has to include pages "Home" "Contact" "Service" and So on at least 6-8 pages. The site is mainly for publicity and promotion. We will have an existing domain and hosting.
Updates

We prefer the original design, thanks.

Target Market(s)

large public art

Industry/Entity Type

Architecture and design, large public art and sculpture manufacturer

Coding

Coded - Design and coding required

Number of Pages Required

5+ page

Requirements
Must have
• 1. the overall color has to match our logo color 2. Do not need to do any change on our logo including the color 3. Here is a similar style of the home page we like, it can be similar but must not same. Pls check the below link. https://www.velmardo.it/en-us/

```html
<!DOCTYPE html>
<html lang="en">
<head>
<meta charset="utf-8">
<title>MVR — The Grand Mural</title>
<link rel="stylesheet" href="https://fonts.googleapis.com/css2?family=Archivo:wdth,wght@62..125,200..900&family=Montserrat:wght@400;500;600;700&display=swap">
<style>
:root{
  --ink:#111111;
  --ink-soft:#333333;
  --text:#4a4a4a;
  --muted:#777777;
  --white:#ffffff;
  --paper:#f4f4f4;
  --line:#2b2b2b;
  --button-edge:#3d4f5c;
  --footer:#0b0b0b;
  --footer-text:#9a9a9a;
  --shade:#a9a9a9;
}
*{margin:0;padding:0;box-sizing:border-box}
html,body{width:1200px;height:4454px;overflow:hidden}
body{font-family:"Montserrat",sans-serif;color:var(--text);background:var(--white);position:relative}
.display{font-family:"Archivo",sans-serif;font-stretch:125%}
section,header,footer{position:absolute;left:0;width:1200px;overflow:hidden}
.abs{position:absolute}

/* header */
.site-header{top:0;height:75px;background:var(--white);z-index:3}
.brand{position:absolute;left:106px;top:14px;display:flex;align-items:center;gap:10px}
.brand-mark{width:14px;height:14px;background:var(--ink)}
.brand-name{font-family:"Archivo",sans-serif;font-stretch:125%;font-weight:800;font-size:34px;color:var(--ink);letter-spacing:1px;line-height:1}
.main-nav{position:absolute;top:27px;left:453px;display:flex;gap:0}
.main-nav a{font-family:"Montserrat",sans-serif;font-size:12px;color:var(--muted);text-decoration:none;position:absolute;white-space:nowrap;text-transform:uppercase}
.main-nav a.active{color:var(--ink);font-weight:700}
.main-nav a.active::after{content:"";position:absolute;left:0;right:0;top:24px;height:2px;background:var(--ink)}

/* hero */
.hero{top:75px;height:720px}
.hero-photo{position:absolute;left:0;top:0;width:1200px;height:663px;background:linear-gradient(110deg,#4a4a4a 0%,#6d6d6d 30%,#a3a3a3 48%,#7a7a7a 62%,#595959 80%,#3f3f3f 100%)}
.hero-title{position:absolute;left:100px;top:215px;font-weight:800;font-size:64px;color:var(--white);letter-spacing:0.5px;line-height:1}
.hero-sub{position:absolute;left:108px;top:302px;font-weight:300;font-size:28px;color:var(--white);letter-spacing:0.5px}
.scroll-hint{position:absolute;left:588px;top:505px}

/* section headings */
.eyebrow{font-size:14px;letter-spacing:1.5px;color:var(--ink-soft);text-transform:uppercase}
.heading{font-family:"Archivo",sans-serif;font-stretch:125%;color:var(--ink);line-height:1;white-space:nowrap}
.heading .light{font-weight:300}
.heading .bold{font-weight:800}
.rule{height:3px;width:52px;background:var(--ink)}
.body-copy{font-size:14.5px;line-height:28px;color:var(--text)}
.btn{display:flex;align-items:center;justify-content:center;font-family:"Montserrat",sans-serif;font-weight:700;font-size:12.5px;letter-spacing:2px;color:var(--ink);border:1.5px solid var(--button-edge);text-decoration:none;background:transparent}

/* about */
.about{top:738px;height:573px;background:var(--white)}
.about-watermark{position:absolute;left:0;width:1200px;top:110px;text-align:center;font-family:"Archivo",sans-serif;font-stretch:125%;font-weight:900;font-size:300px;color:#f2f2f2;line-height:1}

/* services */
.services{top:1311px;height:582px;background:linear-gradient(160deg,#f2f2f2 0%,#e2e2e2 40%,#f7f7f7 70%,#e8e8e8 100%)}
.service-card{position:absolute;overflow:hidden;color:var(--white);text-align:center}
.service-card .photo{position:absolute;inset:0}
.service-card .icon{position:absolute;left:50%;transform:translateX(-50%)}
.service-card .title{position:absolute;left:0;right:0;font-family:"Archivo",sans-serif;font-stretch:125%;font-weight:700;font-size:17px}
.service-card .sub{position:absolute;left:0;right:0;font-family:"Archivo",sans-serif;font-stretch:125%;font-weight:300;font-size:17px}
.service-card .btn{position:absolute;color:var(--white);border:2px solid var(--white);font-size:9px;letter-spacing:2px}

/* split */
.split{top:1893px;height:503px}
.split-panel{position:absolute;top:0;width:600px;height:503px;color:var(--white)}
.split-panel .photo{position:absolute;inset:0}
.split-panel .eyebrow{position:absolute;color:#e8e8e8;font-size:14px}
.split-panel .heading{position:absolute;color:var(--white);font-size:38px}
.split-panel .rule{position:absolute;background:var(--white);width:54px}
.split-panel p{position:absolute;font-size:11.5px;line-height:22px;color:#f0f0f0;width:400px}
.split-panel .link{position:absolute;font-size:14px;font-weight:600;color:var(--white);text-decoration:none;letter-spacing:0.3px}

/* vision */
.vision{top:2396px;height:612px;background:var(--white)}
.vision-art{position:absolute;left:60px;top:40px;width:560px;height:520px;background:radial-gradient(ellipse at 45% 50%,#9a9a9a 0%,#c7c7c7 35%,#ededed 62%,#ffffff 78%)}

/* collections */
.collections{top:3008px;height:557px;background:linear-gradient(90deg,#ececec 0%,#f0f0f0 60%,#e6e6e6 100%)}

/* contact */
.contact{top:3565px;height:498px;background:linear-gradient(150deg,#2c2c2c 0%,#4c4c4c 35%,#3a3a3a 60%,#5a5a5a 100%)}
.contact .heading{color:var(--white)}
.contact .body-copy{color:#dddddd}
.contact .btn{background:var(--white);border:none;color:var(--ink)}

/* footer */
.site-footer{top:4063px;height:391px;background:var(--footer);color:var(--footer-text)}
.site-footer .brand-name{color:var(--white)}
.site-footer .brand-mark{background:var(--white)}
.footer-about{position:absolute;left:125px;top:176px;width:280px;font-size:9.5px;line-height:14px;color:#8a8a8a}
.footer-col{position:absolute;top:99px}
.footer-col h4{font-family:"Montserrat",sans-serif;font-weight:700;font-size:16px;letter-spacing:2px;color:var(--white)}
.footer-col h4::after{content:"";display:block;width:34px;height:2px;background:var(--white);margin-top:10px}
.footer-col ul{list-style:none;margin-top:18px}
.footer-col li{font-size:12px;color:var(--footer-text);height:26.5px;display:flex;align-items:center;gap:12px}
.footer-col .dot{width:24px;height:24px;border-radius:50%;background:#d9d9d9;flex:none}
.footer-col.social li{height:38px}
.footer-base{position:absolute;left:0;right:0;top:348px;border-top:1px solid #1e1e1e;padding-top:10px;text-align:center;font-size:9px;color:#7c7c7c}
</style>
</head>
<body>

<header class="site-header">
  <div class="brand"><span class="brand-mark"></span><span class="brand-name">MVR</span></div>
  <nav class="main-nav">
    <a class="active" href="#" style="left:0">About Us</a>
    <a href="#" style="left:121px">Services</a>
    <a href="#" style="left:233px">Artists</a>
    <a href="#" style="left:338px">Public Art</a>
    <a href="#" style="left:466px">Blogs</a>
    <a href="#" style="left:560px">Contact</a>
  </nav>
</header>

<section class="hero">
  <div class="hero-photo" role="img" aria-label="Black and white photograph of a winged classical marble statue on a stone ship prow inside a museum hall"></div>
  <svg class="abs" style="left:0;top:0" width="1200" height="720" viewBox="0 0 1200 720">
    <polygon points="0,663 1200,615 1200,720 0,720" fill="#ffffff"/>
    <polygon points="605,647 1200,620 1200,707" fill="var(--shade)"/>
  </svg>
  <h1 class="hero-title display">THE GRAND MURAL</h1>
  <p class="hero-sub display">ART &amp; DESIGN AROUND THE WORLD</p>
  <svg class="scroll-hint" width="22" height="44" viewBox="0 0 22 44">
    <rect x="3" y="1" width="16" height="24" rx="8" fill="none" stroke="#fff" stroke-width="1.5"/>
    <line x1="11" y1="6" x2="11" y2="11" stroke="#fff" stroke-width="1.5"/>
    <polyline points="6,30 11,34 16,30" fill="none" stroke="#fff" stroke-width="1.5"/>
    <polyline points="6,36 11,40 16,36" fill="none" stroke="#fff" stroke-width="1.5"/>
  </svg>
</section>

<section class="about">
  <div class="about-watermark" aria-hidden="true">MVR</div>
  <p class="eyebrow abs" style="left:0;width:1190px;top:120px;text-align:center">Who we are</p>
  <h2 class="heading abs" style="left:0;width:1190px;top:146px;text-align:center;font-size:42px"><span class="bold">ABOUT THE GRAND MURAL</span></h2>
  <div class="rule abs" style="left:567px;top:193px"></div>
  <p class="body-copy abs" style="left:180px;width:830px;top:228px;text-align:center">Lorem ipsum dolor sit amet, consectetur adipiscing elit, sed do eiusmod tempor incididunt ut labore et dolore magna aliqua. Ut enim ad minim veniam, quis nostrud Axercitation ullamco laboris nisi ut aliquip ex ea commodo consequat. Duis aute irure dolor in reprehenderit.labore et dolore magna aliqua.</p>
  <a class="btn abs" href="#" style="left:508px;top:341px;width:180px;height:47px">LEARN MORE</a>
</section>

<section class="services">
  <h2 class="heading abs" style="left:0;width:1200px;top:54px;text-align:center;font-size:40px"><span class="light">OUR </span><span class="bold">SERVICES</span></h2>
  <div class="rule abs" style="left:568px;top:104px;width:64px"></div>

  <div class="service-card" style="left:111px;top:186px;width:326px;height:268px">
    <div class="photo" role="img" aria-label="Dark photograph of a modern building facade with angled metal ribs" style="background:linear-gradient(120deg,#2a2a2a,#4a4a4a 45%,#1e1e1e)"></div>
    <svg class="icon" style="top:68px" width="54" height="52" viewBox="0 0 54 52" fill="none" stroke="#fff" stroke-width="2">
      <rect x="3" y="3" width="12" height="16"/><rect x="21" y="3" width="12" height="16"/><rect x="39" y="3" width="12" height="16"/>
      <line x1="10" y1="30" x2="44" y2="30"/><line x1="12" y1="30" x2="12" y2="48"/><line x1="42" y1="30" x2="42" y2="48"/><line x1="6" y1="48" x2="48" y2="48"/>
    </svg>
    <p class="title" style="top:133px">LOREM IPSUM DOLOR</p>
    <p class="sub" style="top:157px">CONSECTETUR</p>
  </div>

  <div class="service-card" style="left:443px;top:159px;width:326px;height:325px">
    <div class="photo" role="img" aria-label="Muted photograph of a contemporary museum building with vertical fins" style="background:linear-gradient(135deg,#555 0%,#7b7b7b 45%,#5e5e5e 75%,#6a6a6a 100%)"></div>
    <svg class="icon" style="top:93px" width="50" height="50" viewBox="0 0 50 50" fill="none" stroke="#fff" stroke-width="2">
      <polygon points="25,3 45,14 5,14"/><line x1="5" y1="18" x2="45" y2="18"/>
      <line x1="11" y1="18" x2="11" y2="40"/><line x1="21" y1="18" x2="21" y2="40"/><line x1="29" y1="18" x2="29" y2="40"/><line x1="39" y1="18" x2="39" y2="40"/>
      <line x1="3" y1="44" x2="47" y2="44"/>
    </svg>
    <p class="title" style="top:160px">LOREM IPSUM DOLOR</p>
    <p class="sub" style="top:184px">CONSECTETUR</p>
    <a class="btn" href="#" style="left:98px;top:221px;width:138px;height:34px">LEARN MORE</a>
  </div>

  <div class="service-card" style="left:775px;top:186px;width:326px;height:268px">
    <div class="photo" role="img" aria-label="Dark photograph of a winged stone sculpture against a wall" style="background:linear-gradient(60deg,#262626,#454545 55%,#2f2f2f)"></div>
    <svg class="icon" style="top:60px" width="46" height="58" viewBox="0 0 46 58" fill="none" stroke="#fff" stroke-width="2">
      <path d="M32 6 A18 18 0 1 0 36 36"/><path d="M28 12 A11 11 0 1 0 32 30"/>
      <line x1="23" y1="44" x2="23" y2="52"/><line x1="8" y1="54" x2="38" y2="54"/>
    </svg>
    <p class="title" style="top:133px">LOREM IPSUM DOLOR</p>
    <p class="sub" style="top:157px">CONSECTETUR</p>
  </div>
</section>

<section class="split">
  <div class="split-panel" style="left:0">
    <div class="photo" role="img" aria-label="Photograph of a concrete gallery interior with a flowing curved wooden sculpture" style="background:linear-gradient(120deg,#6b655f 0%,#8d857c 35%,#9a6b4a 60%,#6e6660 100%)"></div>
    <p class="eyebrow" style="left:111px;top:176px">Public Arts</p>
    <h3 class="heading" style="left:110px;top:200px"><span class="light">ART </span><span class="bold">&amp; DESIGNS</span></h3>
    <div class="rule" style="left:111px;top:245px"></div>
    <p style="left:112px;top:262px">Lorem ipsum dolor sit amet, consectetur adipiscing elit, sed do eiusmod tempor incididunt ut labore et.</p>
    <a class="link" href="#" style="left:113px;top:337px">VIEW MORE</a>
  </div>
  <div class="split-panel" style="left:600px">
    <div class="photo" role="img" aria-label="Photograph of a weathered bronze bust sculpture in a gallery" style="background:linear-gradient(100deg,#7a6e65 0%,#6b5544 40%,#5d4637 65%,#8a7b70 100%)"></div>
    <p class="eyebrow" style="left:106px;top:176px">Our Artists</p>
    <h3 class="heading" style="left:106px;top:200px"><span class="light">MEET </span><span class="bold">ARTISTS</span></h3>
    <div class="rule" style="left:107px;top:245px"></div>
    <p style="left:108px;top:262px">Lorem ipsum dolor sit amet, consectetur adipiscing elit, sed do eiusmod tempor incididunt ut labore et.</p>
    <a class="link" href="#" style="left:110px;top:337px">LEARN MORE</a>
  </div>
</section>

<section class="vision">
  <div class="vision-art" role="img" aria-label="Black and white collage of stone sculpture and architecture photographs"></div>
  <p class="eyebrow abs" style="left:631px;top:139px">Our Artists</p>
  <h2 class="heading abs" style="left:630px;top:162px;font-size:42px"><span class="light">OUR </span><span class="bold">VISION</span></h2>
  <div class="rule abs" style="left:631px;top:212px;width:60px"></div>
  <p class="body-copy abs" style="left:631px;top:240px;width:420px;font-size:13.5px">Lorem ipsum dolor sit amet, consectetur adipiscing elit, sed do eiusmod tempor incididunt ut labore et dolore magna aliqua. Ut enim ad minim veniam, quis nostrud Axercitation ullamco laboris nisi ut aliquip ex ea commodo</p>
  <a class="btn abs" href="#" style="left:634px;top:381px;width:181px;height:48px">LEARN MORE</a>
</section>

<section class="collections">
  <svg class="abs" style="left:0;top:0" width="1200" height="557" viewBox="0 0 1200 557" role="img" aria-label="Photograph of a large colourful sculpture made of recycled materials under a blue sky">
    <defs>
      <linearGradient id="collectionSky" x1="0" y1="0" x2="1" y2="1">
        <stop offset="0" stop-color="#1a63c9"/>
        <stop offset="0.45" stop-color="#3f86d9"/>
        <stop offset="0.7" stop-color="#5f7f7a"/>
        <stop offset="1" stop-color="#8a6d5b"/>
      </linearGradient>
    </defs>
    <polygon points="740,0 1200,0 1200,557 700,557 576,286" fill="url(#collectionSky)"/>
  </svg>
  <p class="eyebrow abs" style="left:121px;top:120px">Our Artists</p>
  <h2 class="heading abs" style="left:120px;top:143px;font-size:42px"><span class="light">OUR </span><span class="bold">COLLECTIONS</span></h2>
  <div class="rule abs" style="left:121px;top:193px;width:60px"></div>
  <p class="body-copy abs" style="left:121px;top:219px;width:420px;font-size:13.5px">Lorem ipsum dolor sit amet, consectetur adipiscing elit, sed do eiusmod tempor incididunt ut labore et dolore magna aliqua. Ut enim ad minim veniam, quis nostrud Axercitation ullamco laboris nisi ut aliquip ex ea commodo</p>
  <a class="btn abs" href="#" style="left:124px;top:357px;width:182px;height:48px">LEARN MORE</a>
</section>

<section class="contact" role="img" aria-label="Dark photograph of a concrete stairway with angled light">
  <svg class="abs" style="left:0;top:0" width="1200" height="498" viewBox="0 0 1200 498">
    <polygon points="588,498 1200,429 1200,498" fill="#9c9c9c"/>
  </svg>
  <h2 class="heading abs" style="left:0;width:1220px;top:128px;text-align:center;font-size:40px"><span class="light">CONTACT </span><span class="bold">MVR</span></h2>
  <p class="body-copy abs" style="left:270px;width:680px;top:196px;text-align:center;font-size:14px">Lorem ipsum dolor sit amet, consectetur adipiscing elit, sed do eiusmod tempor incididunt ut labore et dolore magna aliqua. Ut enim ad minim veniam quis nostrud.</p>
  <a class="btn abs" href="#" style="left:515px;top:275px;width:190px;height:45px">GET IN TOUCH</a>
</section>

<footer class="site-footer">
  <div class="brand" style="left:116px;top:100px"><span class="brand-mark"></span><span class="brand-name">MVR</span></div>
  <p class="footer-about">Lorem ipsum dolor sit amet, consectetur adipiscing elit, sed do eiusmod tempor incididunt ut labore et dolore magna aliqua Ut enim ad minim</p>
  <div class="footer-col" style="left:508px">
    <h4>COMPANY</h4>
    <ul><li>About Us</li><li>Our Services</li><li>Art &amp; Design</li><li>Artists</li></ul>
  </div>
  <div class="footer-col" style="left:701px">
    <h4>RESOURCES</h4>
    <ul><li>Blogs</li><li>Privacy Policy</li><li>Legal</li><li>Contact Us</li></ul>
  </div>
  <div class="footer-col social" style="left:922px">
    <h4>GET IN TOUCH</h4>
    <ul style="margin-top:10px"><li><span class="dot"></span>Friendbook</li><li><span class="dot"></span>Chirper</li><li><span class="dot"></span>Linkwork</li></ul>
  </div>
  <p class="footer-base">© 2021 The Grand Mural | All Rights Reserved</p>
</footer>

</body>
</html>
```